Create a backdrop for a trade show booth!

We are looking for a design to put on a 10'X10' trade show booth for our company: Marlow Frost Jet.

Please see website: www.marlowfrostjet.com

Industry/Entity Type

It Company

```html
<!DOCTYPE html>
<html lang="en">
<head>
<meta charset="utf-8">
<title>Marlow Frost Jet – Trade Show Backdrop</title>
<link rel="stylesheet" href="https://fonts.googleapis.com/css2?family=Cinzel:wght@500&display=swap">
<style>
  :root {
    --stage: #eceff1;
    --navy: #13202e;
    --ice: #5ee8ee;
    --snow: #ffffff;
  }
  * { margin: 0; padding: 0; box-sizing: border-box; }
  html, body {
    width: 785px;
    height: 1200px;
    overflow: hidden;
    background: var(--stage);
  }
  .canvas {
    position: relative;
    width: 785px;
    height: 1200px;
  }
  .backdrop {
    position: absolute;
    left: 32px;
    top: 240px;
    width: 720px;
    height: 720px;
    display: block;
  }
  .brand-type {
    font-family: "Cinzel", "Times New Roman", serif;
    font-weight: 500;
    fill: var(--snow);
  }
  .tile-name { font-size: 8.5px; letter-spacing: 1px; }
  .hero-name { font-size: 46px; letter-spacing: 4px; }
  .ice-dot { fill: var(--ice); }
</style>
</head>
<body>
<main class="canvas">
  <svg class="backdrop" viewBox="0 0 720 720" role="img" aria-label="Marlow Frost Jet step-and-repeat backdrop">
    <defs>
      <pattern id="repeat-row-a" patternUnits="userSpaceOnUse" x="14" y="10" width="102" height="88">
        <g class="repeat-tile">
          <circle class="ice-dot" cx="8" cy="11" r="7"/>
          <text class="brand-type tile-name" x="19" y="9">MARLOW</text>
          <text class="brand-type tile-name" x="19" y="20">FROST JET</text>
        </g>
      </pattern>
      <pattern id="repeat-row-b" patternUnits="userSpaceOnUse" x="65" y="54" width="102" height="88">
        <g class="repeat-tile">
          <circle class="ice-dot" cx="8" cy="11" r="7"/>
          <text class="brand-type tile-name" x="19" y="9">MARLOW</text>
          <text class="brand-type tile-name" x="19" y="20">FROST JET</text>
        </g>
      </pattern>
    </defs>

    <rect class="backdrop-field" width="720" height="720" fill="var(--navy)"/>

    <g class="repeat-upper">
      <rect x="14" y="0" width="714" height="264" fill="url(#repeat-row-a)"/>
      <rect x="65" y="0" width="612" height="264" fill="url(#repeat-row-b)"/>
    </g>
    <g class="repeat-lower">
      <rect x="14" y="450" width="714" height="264" fill="url(#repeat-row-a)"/>
      <rect x="65" y="450" width="612" height="264" fill="url(#repeat-row-b)"/>
    </g>

    <g class="hero-name-block">
      <circle class="ice-dot" cx="175" cy="357" r="60"/>
      <text class="brand-type hero-name" x="265" y="345">MARLOW</text>
      <text class="brand-type hero-name" x="265" y="402">FROST JET</text>
    </g>
  </svg>
</main>
</body>
</html>
```